Australian Apparel Company requires 4 page brochure for Industry

I am looking for a brochure that shows a series of different clothing brands in High Visibility work wear. Each page needs to highlight the products in groups,shorts & short sleeve, long pants and long sleeve. 8 products total and a pair of boots, all images provided. Each section needs to look different with a different industry look, there will be a series of 4 brands in total, background images to be faded on product pages with colour elements to create interest. There needs to be an item code & title & price with each product all details supplied in Workwear brief. Lifestyle logo and industries we supply images needs to be shown in the cover. The last page should be a how to order section and contact details and brief company details. The overall look of the brochure should be clean and modern industrial, showing a different industry background or multiple different industries, I don't want each section to look exactly the same just with different images, but the overall look should be consistent / similar. See Design brief last file uploaded.
Updates

Target Market(s)

Procurement managers, project directors, in multiple industries, within Australia

Industry/Entity Type

Industrial

Font styles to use
Sans Serif

Colors
fbee3d
f36f22
1b1b1b

Requirements
Must have
• Product images and codes, industry backgrounds references.
Nice to have
• Items grouped by Short/Short Sleeve & Pants/Long Sleeve
Should not have
• Overall look should be engaging with different the industry professionals from mining, construction, automotive industries but not too busy to detract from products.

```html
<!DOCTYPE html>
<html lang="en">
<head>
<meta charset="utf-8">
<title>Rock Solid Dependability – Keystone Apparel</title>
<link href="https://fonts.googleapis.com/css2?family=Russo+One&family=Montserrat:wght@500&display=swap" rel="stylesheet">
<style>
  :root {
    --yellow: #fcc21b;
    --black: #141414;
    --ink: #1b1b1b;
    --white: #ffffff;
    --grey: #bdbdbd;
    --tread: #3a3a3a;
    --rivet: #555555;
  }
  * { margin: 0; padding: 0; box-sizing: border-box; }
  html, body { width: 847px; height: 1200px; overflow: hidden; background: var(--white); }
  .cover { position: relative; width: 847px; height: 1200px; background: var(--white); font-family: "Russo One", sans-serif; }

  .industry-photo { position: absolute; top: 0; height: 170px; }
  .industry-photo--backhoe { left: 0; width: 272px; background: linear-gradient(160deg, #6f9a4a 0%, #c9a224 55%, #5b4a33 100%); }
  .industry-photo--mine { left: 284px; width: 274px; background: linear-gradient(180deg, #a7a9a6 0%, #7d776b 50%, #9c8b72 100%); }
  .industry-photo--excavator { left: 571px; width: 276px; background: linear-gradient(180deg, #8cc0e8 0%, #cfa34a 55%, #a96f45 100%); }

  .hero { position: absolute; top: 182px; left: 0; width: 847px; height: 486px; background: var(--black); overflow: hidden; }
  .hero__tread { position: absolute; top: -40px; right: -60px; width: 300px; height: 620px; transform: rotate(14deg);
    background: linear-gradient(90deg, transparent 0%, var(--tread) 20%, var(--tread) 80%, transparent 100%); opacity: .55; }

  .brand { position: absolute; top: 96px; left: 0; width: 847px; text-align: center; color: var(--grey); }
  .brand__name { font-family: "Montserrat", sans-serif; font-weight: 500; font-size: 30px; letter-spacing: 1px; display: inline-flex; align-items: center; gap: 10px; }
  .brand__mark { width: 12px; height: 12px; background: var(--yellow); display: inline-block; }

  .headline { position: absolute; left: 100px; top: 212px; transform: rotate(-4deg); transform-origin: left top; line-height: .92; font-weight: 400; }
  .headline__rock { color: var(--yellow); font-size: 108px; }
  .headline__solid { color: var(--white); font-size: 108px; }
  .headline__dependability { display: block; color: var(--yellow); font-size: 78px; letter-spacing: -1px; }
  .headline__services-tag { display: block; color: var(--white); font-size: 39px; margin-top: 4px; }

  .services { position: absolute; left: 0; top: 462px; width: 847px; text-align: center; color: var(--yellow); font-size: 13.5px; letter-spacing: .3px; white-space: nowrap; }

  .cover-band { position: absolute; top: 668px; left: 0; width: 847px; height: 134px; background: var(--yellow); }
  .cover-band__rivets { position: absolute; left: 0; width: 847px; height: 8px; }
  .cover-band__rivets--top { top: 11px; }
  .cover-band__rivets--bottom { bottom: 8px; }
  .cover-band__slogan { position: absolute; top: 36px; width: 847px; text-align: center; color: var(--ink); font-size: 52px; letter-spacing: 3px; white-space: nowrap; }

  .site-photo { position: absolute; top: 802px; left: 0; width: 847px; height: 398px;
    background: linear-gradient(180deg, #9fb98a 0%, #d9d6cf 35%, #c9231e 62%, #b9a58a 100%); }
</style>
</head>
<body>
<main class="cover">
  <div class="industry-photo industry-photo--backhoe" role="img" aria-label="Yellow backhoe loader working on a grassy site"></div>
  <div class="industry-photo industry-photo--mine" role="img" aria-label="Bucket-wheel excavator in an open-cut mine"></div>
  <div class="industry-photo industry-photo--excavator" role="img" aria-label="Yellow excavator digging in earth under blue sky"></div>

  <section class="hero">
    <div class="hero__tread" role="img" aria-label="Faint tyre tread texture"></div>
    <div class="brand">
      <span class="brand__name"><span class="brand__mark"></span>Keystone Apparel</span>
    </div>
    <h1 class="headline">
      <span class="headline__rock">ROCK</span><span class="headline__solid">SOLID</span>
      <span class="headline__dependability">DEPENDABILITY</span>
      <span class="headline__services-tag">PRINT_STITCH_STYLE</span>
    </h1>
    <p class="services">SCREEN PRINTING • SUBLIMINATION • MARKETING • BRANDING • PRINTING • UNIFORM SUPPLY SOLUTIONS</p>
  </section>

  <section class="cover-band">
    <svg class="cover-band__rivets cover-band__rivets--top" viewBox="0 0 847 8" aria-hidden="true">
      <pattern id="rivet" width="36" height="8" patternUnits="userSpaceOnUse"><circle cx="20" cy="4" r="3" fill="#555"/></pattern>
      <rect width="847" height="8" fill="url(#rivet)"/>
    </svg>
    <p class="cover-band__slogan">WE'VE GOT YOU COVERED!</p>
    <svg class="cover-band__rivets cover-band__rivets--bottom" viewBox="0 0 847 8" aria-hidden="true">
      <rect width="847" height="8" fill="url(#rivet)"/>
    </svg>
  </section>

  <div class="site-photo" role="img" aria-label="Red mobile crane beside scaffolding on a house construction site"></div>
</main>
</body>
</html>
```